Photographic Tutorial website

We are looking for a fresh design for a photographic tutorial / workshop website. The website will have the included functions:

* Home (needs to have a login section)
* About Us
* Info about each course / workshop.
* Subscribe to courses and pay online.
* Members Area
* Photo gallery
* Contact us

The website will be implemented with our own made cms. We do not need it to be coded. We have a team ready to do this for us. We only need the PSD layout.

We have attached a mockup design that the client and I have come up with and we need the design to be taken to the next level.

Client also likes:
http://www.lumavistacamera.example/

Requirements
Must have
• Must Stand out i.e black backgrounds
Should not have
• Alter the logo in anyway.

```html
<!DOCTYPE html>
<html lang="en">
<head>
<meta charset="utf-8">
<title>Aperture Pal – Photographic Tuition</title>
<link rel="stylesheet" href="https://fonts.googleapis.com/css2?family=Arimo:wght@400;700&family=Gelasio:ital,wght@1,700&display=swap">
<style>
:root{
  --bg-grey:#3d3d3d;
  --bg-dark:#151515;
  --panel:#2e2e2e;
  --panel-edge:#555;
  --green:#7db527;
  --green-dark:#4f7f12;
  --text:#e6e6e6;
  --muted:#aaaaaa;
  --accent:#ffd200;
  --frame:#d9d9d9;
}
*{box-sizing:border-box;margin:0;padding:0}
html,body{width:1200px;height:1161px;overflow:hidden}
body{position:relative;background:var(--bg-grey);font-family:"Arimo",Arial,sans-serif;color:var(--text)}
.abs{position:absolute}
.serif{font-family:"Gelasio",Georgia,serif;font-style:italic;font-weight:700;white-space:nowrap}

.header{left:0;top:0;width:1200px;height:152px;background:linear-gradient(#4a4a4a,#383838);border-top:3px solid #6b8a2a}
.brand{left:168px;top:22px;display:flex;align-items:center;gap:10px}
.brand-dot{width:38px;height:38px;border-radius:50%;background:var(--green)}
.brand-name{font-size:30px;font-weight:700;color:#fff}
.account{left:826px;top:21px;font-size:13px;color:#fff}
.account b{margin-right:14px}
.search{left:790px;top:49px;width:242px;height:25px;display:flex}
.search-field{flex:1;background:linear-gradient(#111,#2a2a2a);border:1px solid #666;border-right:none;font-size:11px;color:#aaa;display:flex;align-items:center;padding-left:8px;gap:6px}
.search-go{width:28px;background:var(--green);border:1px solid #9bd444;color:#fff;font-weight:700;font-size:13px;font-style:italic;display:flex;align-items:center;justify-content:center}
.nav{left:165px;top:90px;width:867px;height:37px;display:flex;background:linear-gradient(#333,#1c1c1c);border:1px solid #555;border-radius:3px;box-shadow:0 4px 8px rgba(0,0,0,.5)}
.nav a{flex:auto;display:flex;align-items:center;justify-content:center;font-family:"Gelasio",Georgia,serif;font-style:italic;font-size:14.5px;color:#ccc;text-decoration:none;border-right:1px solid #111;white-space:nowrap}
.nav a:last-child{border-right:none}
.nav a.active{background:linear-gradient(#8fcb35,#5d9418);color:#fff;flex:0 0 92px}

.hero-band{left:0;top:152px;width:1200px;height:274px;background:var(--bg-dark);border-top:1px solid #555;border-bottom:1px solid #555}
.hero{left:168px;top:170px;width:864px;height:236px;border:4px solid var(--frame);border-radius:3px;background:linear-gradient(100deg,#3c3430,#c9c2b6 40%,#e3ddd2 60%,#6e5b4c)}

.category{width:204px}
.cat-label{height:26px;background:linear-gradient(#8fcb35,#5d9418);border-radius:3px;text-align:center;font-size:16px;color:#fff;line-height:26px}
.cat-thumb{margin-top:13px;height:100px;border:3px solid var(--frame);border-radius:3px;box-shadow:0 6px 10px rgba(0,0,0,.6)}
.content-rule{left:0;top:600px;width:1200px;height:2px;background:#222;border-bottom:1px solid #555}

.box{background:var(--panel);border:1px solid var(--panel-edge);border-radius:3px}
.box-head{height:31px;background:#0d0d0d;color:#fff;font-family:"Gelasio",Georgia,serif;font-weight:700;font-size:12.5px;text-align:center;line-height:31px;letter-spacing:.3px;white-space:nowrap}
.cat-list{list-style:none}
.cat-list li{height:32px;line-height:32px;padding-left:18px;font-size:11px;font-weight:700;color:#ddd;border-bottom:1px dashed #555}
.cat-list li.current{background:var(--green);color:#111}
.blog-entry{padding:10px 8px 6px;border-bottom:1px dashed #555}
.blog-entry:last-child{border-bottom:none}
.blog-name{font-size:11px;font-weight:700;color:#fff}
.blog-date{font-size:11px;color:var(--muted)}
.blog-text{margin-top:14px;font-size:11px;line-height:13px;text-align:justify;color:#ddd}
.more{display:block;margin:6px 0 0 auto;width:52px;height:14px;background:#0d0d0d;color:var(--accent);font-size:11px;text-align:center;line-height:14px}

.welcome-title{left:387px;top:620px;font-size:22px;color:#fff}
.welcome-rule{left:387px;top:652px;width:426px;height:1px;background:#666}
.welcome-text{left:387px;top:664px;width:288px;font-size:11px;line-height:13px;color:#ddd}
.welcome-text p+p{margin-top:13px}
.welcome-photo{left:694px;top:668px;width:116px;height:124px;border:4px solid #eee;background:linear-gradient(#2f4b22,#7a8c5a,#3c3a28);transform:rotate(2deg);box-shadow:3px 5px 8px rgba(0,0,0,.6)}

.testimonial-body{padding:14px 10px 0 10px;font-size:11px;line-height:13px;color:#ddd;text-align:justify}
.quote-mark{color:var(--green);font-size:20px;font-weight:700;line-height:10px}
.testimonial-by{text-align:right;margin-top:14px;font-weight:700;color:var(--green);font-size:11px}
.testimonial-date{text-align:right;color:var(--muted);font-size:11px}

.section-title{font-size:19px;color:#fff}
.gallery-grid{left:392px;top:897px;width:370px;height:158px;border:2px solid #ddd;display:grid;grid-template-columns:repeat(3,1fr);grid-template-rows:1fr 1fr;gap:2px;background:#ddd}
.btn{height:17px;padding:0 9px;background:linear-gradient(#8fcb35,#5d9418);border-radius:2px;color:#fff;font-size:11px;font-weight:700;line-height:17px}
.video{left:810px;top:897px;width:196px;height:158px;background:#000;border:1px solid #444}
.video-title{position:absolute;left:8px;top:4px;font-size:11px;color:#fff}
.video-screen{position:absolute;left:0;top:20px;width:194px;height:112px;background:linear-gradient(120deg,#5a6a1e,#9aa43c 50%,#4a4a20)}
.video-bar{position:absolute;left:0;bottom:0;width:194px;height:24px;background:linear-gradient(#333,#111);font-size:9px;color:#bbb;display:flex;align-items:center;gap:8px;padding-left:10px}

.footer{left:0;top:1112px;width:1200px;height:49px;background:#111;border-top:1px solid #555}
.copyright{left:168px;top:1137px;font-size:11px;color:#ccc}
.find-us{left:828px;top:1124px;font-size:22px;color:#fff}
.social{width:28px;height:28px;border-radius:4px;background:#3d8fd1;top:1124px}
</style>
</head>
<body>

<header class="abs header">
  <div class="abs brand"><span class="brand-dot"></span><span class="brand-name">Aperture Pal</span></div>
  <div class="abs account"><b>Welcome Guest !</b>Login &nbsp;/&nbsp; Sign up</div>
  <div class="abs search">
    <div class="search-field">
      <svg width="14" height="14" viewBox="0 0 14 14"><circle cx="8" cy="6" r="4" fill="none" stroke="#ccc" stroke-width="1.6"/><line x1="5" y1="9" x2="1" y2="13" stroke="#ccc" stroke-width="2"/></svg>
      Search...
    </div>
    <div class="search-go">GO</div>
  </div>
  <nav class="abs nav">
    <a class="active" href="#">Home</a><a href="#">About Us</a><a href="#">Our Course</a><a href="#">Online Payment</a><a href="#">Members Area</a><a href="#">Photo gallery</a><a href="#">Contact us</a>
  </nav>
</header>

<section class="abs hero-band"></section>
<div class="abs hero" role="img" aria-label="Banner photo of a stylishly dressed couple posing in a vintage room with a mirror"></div>

<div class="abs category" style="left:165px;top:437px"><div class="cat-label serif">Excursion</div><div class="cat-thumb" role="img" aria-label="Group of people in life jackets on a boat" style="background:linear-gradient(#6f8fae,#a6573e 60%,#3a4d66)"></div></div>
<div class="abs category" style="left:387px;top:437px"><div class="cat-label serif">Wedding</div><div class="cat-thumb" role="img" aria-label="Bride and groom among leaves" style="background:linear-gradient(100deg,#7f9a4a,#e8e4dc 55%,#3b2f2a)"></div></div>
<div class="abs category" style="left:608px;top:437px"><div class="cat-label serif">Night city</div><div class="cat-thumb" role="img" aria-label="City skyline lit up at night under a bridge" style="background:linear-gradient(#1a1a22,#2b2530 55%,#b07a2a 75%,#1a1410)"></div></div>
<div class="abs category" style="left:828px;top:437px"><div class="cat-label serif">Potrait</div><div class="cat-thumb" role="img" aria-label="Portrait of a woman in a cap" style="background:linear-gradient(100deg,#2b2b2b,#b8866a 55%,#3a3a3a)"></div></div>

<div class="abs content-rule"></div>

<aside class="abs box" style="left:165px;top:617px;width:204px">
  <div class="box-head">BROWSE CATEGORIES</div>
  <ul class="cat-list">
    <li class="current">Concepts &amp; Terminology</li>
    <li>Using Camera Equipment</li>
    <li>Editing &amp; Post-Processing</li>
    <li>Color Management &amp; Printing</li>
    <li style="border-bottom:none">Photo Techniques &amp; Styles</li>
  </ul>
</aside>

<aside class="abs box" style="left:165px;top:827px;width:204px;height:263px">
  <div class="box-head" style="font-size:13px">PHOTOGRAPHY BLOG</div>
  <div class="blog-entry">
    <div class="blog-name">NICK</div><div class="blog-date">10th July'12</div>
    <p class="blog-text">Lorem Ipsum is simply dummy text of the printing and typesetting industry. Lorem Ipsum has been the industry's standard ....</p>
    <span class="more">more...</span>
  </div>
  <div class="blog-entry">
    <div class="blog-name">JOHN</div><div class="blog-date">12th June'12</div>
    <p class="blog-text">Lorem Ipsum is simply dummy text of the printing and typesetting industry. Lorem Ipsum has been the ....</p>
    <span class="more">more...</span>
  </div>
</aside>

<h1 class="abs welcome-title serif">Welcome to Our Site</h1>
<div class="abs welcome-rule"></div>
<div class="abs welcome-text">
  <p>Lorem Ipsum is simply dummy text of the printing and type-setting industry. Lorem Ipsum has been the industry's standard dummy text ever since the 1500s, when an unknown printer took a galley of type and scrambled it to make a type specimen book.</p>
  <p>Lorem Ipsum is simply dummy text of the printing and type-setting industry. Lorem Ipsum has been the industry's standard dummy text ever since the 1500s, when an unknown printer took a galley of type and scrambled it to make a type specimen book.</p>
</div>
<div class="abs welcome-photo" role="img" aria-label="Lush green forest trail"></div>

<aside class="abs box" style="left:828px;top:617px;width:204px;height:209px">
  <div class="box-head">CLIENT TESTIMONIALS</div>
  <div class="testimonial-body">
    <p><span class="quote-mark">&ldquo;</span> Lorem Ipsum is simply dummy text of the printing and typesetting industry. Lorem Ipsum has been the industry's standard dummy text ever since the 1500s, when an unknown printer took a galley of type and scrambled it to make a type specimen book.</p>
    <p class="testimonial-by">Houston</p>
    <p class="testimonial-date">5th July,2012</p>
    <span class="more" style="margin-top:6px">more...</span>
  </div>
</aside>

<section class="abs box" style="left:382px;top:844px;width:648px;height:246px">
  <h2 class="abs section-title serif" style="left:13px;top:10px">Members Gallery</h2>
  <div class="abs" style="left:10px;top:40px;width:370px;height:1px;background:#666"></div>
  <div class="abs" style="left:399px;top:12px;width:1px;height:222px;background:#666"></div>
  <h2 class="abs section-title serif" style="left:422px;top:10px">Workshops Segment</h2>
  <div class="abs" style="left:422px;top:40px;width:214px;height:1px;background:#666"></div>
</section>
<div class="abs gallery-grid">
  <div role="img" aria-label="Desert rock formations" style="background:linear-gradient(#6a8cc0,#a0522d)"></div>
  <div role="img" aria-label="Orange flowers" style="background:linear-gradient(135deg,#e07a10,#f3a825)"></div>
  <div role="img" aria-label="Green leaves with small pink flowers" style="background:linear-gradient(135deg,#1f4a1c,#4f8a3a)"></div>
  <div role="img" aria-label="Sea turtle swimming" style="background:linear-gradient(135deg,#0d5a9a,#3ea0d0)"></div>
  <div role="img" aria-label="Autumn tree in a field" style="background:linear-gradient(#8a7a3a,#c98a2a 50%,#5a7a2a)"></div>
  <div role="img" aria-label="Bird perched on a branch" style="background:linear-gradient(135deg,#2e4a24,#6a8a3a)"></div>
</div>
<span class="abs btn" style="left:545px;top:1066px">View More</span>

<div class="abs video">
  <span class="video-title">Nature Photography</span>
  <div class="video-screen" role="img" aria-label="Video still of hands holding a camera lens outdoors">
    <svg class="abs" style="left:79px;top:38px" width="36" height="30" viewBox="0 0 36 30"><rect width="36" height="30" rx="6" fill="#111" opacity=".85"/><path d="M14 8 L25 15 L14 22 Z" fill="#fff"/></svg>
  </div>
  <div class="video-bar">
    <svg width="10" height="10" viewBox="0 0 10 10"><path d="M1 0 L9 5 L1 10 Z" fill="#ccc"/></svg>
    <span>0:00 / 4:02</span>
  </div>
</div>
<span class="abs btn" style="left:879px;top:1066px">View More</span>

<footer class="abs footer"></footer>
<p class="abs copyright">Copyright © All images 2012 Aperture Pal. All Right Reserved.</p>
<p class="abs find-us serif">Find us on</p>
<span class="abs social" style="left:962px" aria-label="Social profile"></span>
<span class="abs social" style="left:1002px" aria-label="Social profile"></span>

</body>
</html>
```